Coffee Bag Label

I need label design for both front and back of the coffee bag. I already have had many friends work on it over the past few years and have been selling coffee for two years now. I'm ready to take the next step and expand the business. I live in Nicaragua and sell a lot there, but my main focus is the States and I also want the design to be global friendly. I plan to try and get the product in Europe and Asia. I want to distribute the coffee to large and small stores for resell. I will upload some work done. I like our logo and background art as a friend actually painted it for me. I use white gloss bags and it has a valve on the front. I want the label to be squared from the valve to bottom of bag and sides. The back label can be taller and just a matching template and I can add most of the info on the farm and the coffee. I'm looking for either clean and simple or bright and colorful... I want it to stand out to people around the world as a high quality coffee. I sell single source coffee from one farm and it has all the qualities of the best coffee in the world. I would like to be able to clean up the front label and not have to have all the key features on the front and let the image sell itself. I think the main features of my coffee are that it is high altitude and single source.
Updates

Target Market(s)

America, Nicaragua, Europe and Asia

Industry/Entity Type

Business

Requirements
Must have
• The psd file. Either one main label in which I have three, because I will print one for dark roast, medium roast and ground. Or, one main label with a small blank space for me to place a small sticker saying dark, medium, ground or expresso... This little sticker can be very very simple yet unique maybe? in shape... Design for labels/stickers to place on the white bag.
Nice to have
• I like my logo, but I'm open to it being cleaned up or other font options... The label could possible by odd shaped in look, but clear edges for a simple square label. I like the colors of my logo... but am open to change. Remember, my bags are gloss white.
Should not have
• Main goal is to keep all costs in printing super low, so crazy shaped or foil print is not a good idea as my costs in printing will double. I can not have design all over the bag as I can not afford to print to bag yet. We are not designing the whole coffee bag, just the label for the front and back.

```html
<!DOCTYPE html>
<html lang="en">
<head>
<meta charset="utf-8">
<title>Ridgeline Coffee – Front and Back Bag Labels</title>
<link href="https://fonts.googleapis.com/css2?family=Lilita+One&family=Special+Elite&display=swap" rel="stylesheet">
<style>
  :root {
    --page: #ffffff;
    --leaf-dark: #0f7a1c;
    --leaf-mid: #39b539;
    --leaf-light: #9bf29b;
    --leaf-deep: #0a5c14;
    --cream: #ebebd6;
    --disc: #e6e4df;
    --brown: #4a2a17;
    --ribbon: #2e9a4c;
    --ribbon-dark: #1d6e35;
    --ribbon-text: #4a2a17;
    --scene-sky: #f6c52b;
    --scene-warm: #e8912a;
    --scene-green: #2f9a3a;
    --scene-red: #c8402a;
    --caption-band: rgba(70, 70, 60, 0.45);
    --caption-text: #1c1c18;
  }
  * { margin: 0; padding: 0; box-sizing: border-box; }
  html, body { width: 1200px; height: 1000px; overflow: hidden; background: var(--page); }
  .canvas { position: relative; width: 1200px; height: 1000px; }

  .label { position: absolute; top: 22px; height: 963px; overflow: hidden; }
  .label--front { left: 22px; width: 623px; }
  .label--back { left: 668px; width: 504px; }

  .leaf-field {
    position: absolute; inset: 0;
    background:
      radial-gradient(circle at 10% 15%, var(--leaf-light) 0, transparent 22%),
      radial-gradient(circle at 90% 30%, var(--leaf-light) 0, transparent 20%),
      radial-gradient(circle at 15% 60%, var(--leaf-deep) 0, transparent 25%),
      radial-gradient(circle at 85% 85%, var(--leaf-light) 0, transparent 22%),
      radial-gradient(circle at 20% 92%, var(--leaf-light) 0, transparent 18%),
      radial-gradient(circle at 70% 55%, var(--leaf-deep) 0, transparent 25%),
      linear-gradient(135deg, var(--leaf-mid), var(--leaf-dark) 50%, var(--leaf-mid));
  }

  .brand-disc {
    position: absolute; border-radius: 50%;
    background: var(--disc);
    display: flex; align-items: center; justify-content: center;
  }
  .brand-disc--front { left: 61px; top: 10px; width: 500px; height: 500px; }
  .brand-disc--back { left: 111px; top: 678px; width: 276px; height: 276px; }
  .brand-ring { position: absolute; inset: 0; width: 100%; height: 100%; }
  .ring-text {
    font-family: "Special Elite", monospace;
    font-variant: small-caps;
    font-size: 30px; letter-spacing: 3px;
    fill: var(--brown);
  }
  .brand-name {
    position: relative;
    font-family: "Lilita One", sans-serif;
    color: var(--brown);
    text-align: center;
    line-height: 1.05;
  }
  .brand-disc--front .brand-name { font-size: 72px; }
  .brand-disc--back .brand-name { font-size: 40px; }

  .ribbon { position: absolute; left: 42px; top: 523px; width: 540px; height: 190px; z-index: 3; }
  .ribbon-text { font-family: "Lilita One", sans-serif; fill: var(--ribbon-text); }

  .scene {
    position: absolute; left: 0; top: 606px; width: 623px; height: 357px;
    background:
      radial-gradient(ellipse at 88% 55%, var(--scene-green) 0, transparent 30%),
      radial-gradient(ellipse at 25% 78%, var(--scene-red) 0, transparent 20%),
      linear-gradient(160deg, var(--scene-sky), var(--scene-warm) 70%, var(--scene-sky));
  }

  .caption {
    position: absolute; left: 0; bottom: 0; width: 623px; height: 70px;
    background: var(--caption-band);
    font-family: "Special Elite", monospace;
    color: var(--caption-text);
    text-align: center; z-index: 2;
  }
  .caption-features { font-size: 17px; letter-spacing: 1.5px; font-variant: small-caps; padding-top: 8px; }
  .caption-weight { font-size: 24px; letter-spacing: 1px; padding-top: 2px; }

  .info-panel {
    position: absolute; left: 67px; top: 93px; width: 380px; height: 760px;
    background: var(--cream); border-radius: 26px;
  }
</style>
</head>
<body>
<main class="canvas">

  <section class="label label--front" aria-label="Front label">
    <div class="leaf-field" role="img" aria-label="Painted background of overlapping green coffee leaves"></div>

    <div class="brand-disc brand-disc--front">
      <svg class="brand-ring" viewBox="0 0 500 500" aria-hidden="true">
        <path id="ring-top-front" d="M40 250 A210 210 0 0 1 460 250" fill="none"/>
        <path id="ring-bottom-front" d="M18 250 A232 232 0 0 0 482 250" fill="none"/>
        <text class="ring-text"><textPath href="#ring-top-front" startOffset="50%" text-anchor="middle">Premium Quality • Specialty Bean</textPath></text>
        <text class="ring-text"><textPath href="#ring-bottom-front" startOffset="50%" text-anchor="middle">Single Origin • Direct Trade</textPath></text>
      </svg>
      <p class="brand-name">Ridgeline<br>Coffee</p>
    </div>

    <div class="scene" role="img" aria-label="Painted scene of a farmer in a straw hat holding a cup of coffee and a guitar, with a church and farmhouse behind"></div>

    <svg class="ribbon" viewBox="0 0 540 190" aria-label="Origin and roast">
      <path d="M10 165 L32 188 L46 150 Z" fill="var(--ribbon-dark)"/>
      <path d="M530 160 L508 185 L494 146 Z" fill="var(--ribbon-dark)"/>
      <path d="M20 95 Q270 -50 520 95 L530 160 Q270 90 10 165 Z" fill="var(--ribbon)"/>
      <path id="ribbon-line-one" d="M55 95 Q270 25 485 95" fill="none"/>
      <path id="ribbon-line-two" d="M40 140 Q270 70 500 140" fill="none"/>
      <text class="ribbon-text" font-size="28"><textPath href="#ribbon-line-one" startOffset="50%" text-anchor="middle">MATAGALPA, NICARAGUA</textPath></text>
      <text class="ribbon-text" font-size="42"><textPath href="#ribbon-line-two" startOffset="50%" text-anchor="middle">MEDIUM ROAST</textPath></text>
    </svg>

    <div class="caption">
      <p class="caption-features">100% Arabica • High Altitude • Shade Grown</p>
      <p class="caption-weight">NET WT 16oz 1lb (460grams)</p>
    </div>
  </section>

  <section class="label label--back" aria-label="Back label">
    <div class="leaf-field" role="img" aria-label="Painted background of overlapping green coffee leaves"></div>
    <div class="info-panel"></div>
    <div class="brand-disc brand-disc--back">
      <svg class="brand-ring" viewBox="0 0 500 500" aria-hidden="true">
        <path id="ring-top-back" d="M40 250 A210 210 0 0 1 460 250" fill="none"/>
        <path id="ring-bottom-back" d="M18 250 A232 232 0 0 0 482 250" fill="none"/>
        <text class="ring-text"><textPath href="#ring-top-back" startOffset="50%" text-anchor="middle">Premium Quality • Specialty Bean</textPath></text>
        <text class="ring-text"><textPath href="#ring-bottom-back" startOffset="50%" text-anchor="middle">Single Origin • Direct Trade</textPath></text>
      </svg>
      <p class="brand-name">Ridgeline<br>Coffee</p>
    </div>
  </section>

</main>
</body>
</html>
```